vantaline7 - a safety solution for schools

A Amok App for schools needs your help to design some screens. Its important to have a very simple use of the app. The function of the app is very easy, you put the button to trigger the alarm. The app has a message function. So we need 3 howto screens. you find a better description of the project in the briefing-file. If you have any questions just ask. Thanks in advance for the suggestions. Best Regards, Mert

Target Market(s)

Schools

Industry/Entity Type

Security Service

Font styles to use
Sans Serif

Colors

Designer to choose colors to be used in the design.

Requirements
Must have
• Simple, easy to use, look like a security app, trust,

```html
<!DOCTYPE html>
<html lang="de">
<head>
<meta charset="utf-8">
<title>vantaline7 – App Screens</title>
<link rel="stylesheet" href="https://fonts.googleapis.com/css2?family=Figtree:wght@400;500;800;900&display=swap">
<style>
  :root {
    --bg: #000000;
    --glow: #3a0003;
    --screen-top: #6b0c10;
    --screen-mid: #2a0608;
    --screen-bottom: #151414;
    --yellow: #f5c62a;
    --cyan: #19e3d6;
    --alarm: #e4161c;
    --alarm-dark: #5a0508;
    --ring: #2b0406;
  }
  * { box-sizing: border-box; margin: 0; padding: 0; }
  html, body { width: 1200px; height: 1200px; overflow: hidden; }
  body {
    position: relative;
    font-family: "Figtree", sans-serif;
    background:
      radial-gradient(circle at 20% 30%, var(--glow) 0%, rgba(0,0,0,0) 40%),
      radial-gradient(circle at 80% 50%, #200002 0%, rgba(0,0,0,0) 45%),
      var(--bg);
  }
  .screen {
    position: absolute;
    width: 290px;
    height: 513px;
    overflow: hidden;
    background: linear-gradient(180deg, var(--screen-top) 0%, var(--screen-mid) 45%, var(--screen-bottom) 68%, var(--screen-bottom) 100%);
    text-align: center;
  }
  .screen--splash { left: 91px; top: 331px; width: 367px; height: 650px; }
  .screen--signup { left: 525px; top: 74px; }
  .screen--demo { left: 836px; top: 74px; }
  .screen--cancel { left: 525px; top: 614px; }
  .screen--office { left: 836px; top: 614px; }

  .splash-photo {
    position: absolute; inset: 0;
    background:
      radial-gradient(ellipse at 85% 65%, rgba(70,20,40,0.55) 0%, rgba(0,0,0,0) 45%),
      linear-gradient(180deg, #6e0f12 0%, #4a0a0c 40%, #2a1a22 65%, #141416 100%);
  }
  .splash-brand {
    position: absolute; left: 0; right: 0; top: 508px;
    display: flex; align-items: center; justify-content: center; gap: 10px;
  }
  .splash-brand__dot { width: 14px; height: 14px; border-radius: 50%; background: var(--yellow); }
  .splash-brand__name { font-size: 35px; font-weight: 800; color: var(--cyan); letter-spacing: 0.2px; }
  .splash-tagline {
    position: absolute; left: 0; right: 0; top: 568px;
    font-size: 17px; color: var(--yellow); font-weight: 500;
  }

  .signup-fields { position: absolute; left: 0; right: 0; top: 238px; list-style: none; }
  .signup-fields li { font-size: 13px; color: var(--yellow); height: 44px; letter-spacing: 0.2px; }
  .signup-fields li:nth-child(3) { height: 47px; }
  .signup-fields li:nth-child(n+3) { opacity: 0.8; }

  .siren { position: absolute; left: 105px; top: 292px; }
  .screen-title {
    position: absolute; left: 0; right: 0;
    font-weight: 900; color: var(--yellow); line-height: 1;
  }
  .demo-title { top: 362px; font-size: 24px; }
  .demo-text { position: absolute; left: 0; right: 0; top: 396px; font-size: 13px; color: var(--yellow); line-height: 1.3; }

  .toolbar {
    position: absolute; left: 0; right: 0; bottom: 38px;
    display: flex; justify-content: center; gap: 53px;
  }

  .dial { position: absolute; left: 57px; top: 110px; }
  .cancel-title { top: 382px; font-size: 25px; line-height: 1.05; }
  .office-label { position: absolute; left: 0; right: 0; top: 368px; font-size: 21px; color: var(--yellow); }
  .office-title { top: 389px; font-size: 21px; line-height: 1.05; }
</style>
</head>
<body>

<section class="screen screen--splash">
  <div class="splash-photo" role="img" aria-label="Foto: Schülerin mit Rucksack vor einem Schulgebäude in der Abenddämmerung, rot eingefärbt"></div>
  <div class="splash-brand">
    <span class="splash-brand__dot"></span>
    <span class="splash-brand__name">vantaline7</span>
  </div>
  <p class="splash-tagline">Weil Sicherheit Priorität hat!</p>
</section>

<section class="screen screen--signup">
  <ul class="signup-fields">
    <li>VORNAME</li>
    <li>NACHNAME</li>
    <li>EMAIL ADRESS</li>
    <li>SCHULE</li>
  </ul>
</section>

<section class="screen screen--demo">
  <svg class="siren" width="84" height="44" viewBox="0 0 84 44" aria-hidden="true">
    <g stroke="var(--yellow)" stroke-width="2.5" stroke-linecap="round">
      <line x1="6" y1="4" x2="16" y2="10"/><line x1="2" y1="20" x2="14" y2="20"/><line x1="6" y1="34" x2="16" y2="29"/>
      <line x1="78" y1="4" x2="68" y2="10"/><line x1="82" y1="20" x2="70" y2="20"/><line x1="78" y1="34" x2="68" y2="29"/>
    </g>
    <path d="M26 38 V20 a16 16 0 0 1 32 0 V38 Z" fill="var(--yellow)"/>
    <rect x="38" y="20" width="5" height="18" fill="#e89a12"/>
    <rect x="22" y="38" width="40" height="5" rx="1" fill="#b8860f"/>
  </svg>
  <h2 class="screen-title demo-title">DEMO MODUS</h2>
  <p class="demo-text">Teste den Alarm einmal, bevor<br>du im Notfall wirklich brauchst.</p>
  <nav class="toolbar">
    <svg width="20" height="20" viewBox="0 0 24 24" aria-label="Einstellungen"><path fill="var(--cyan)" d="M19.4 13a7.5 7.5 0 0 0 0-2l2.1-1.6-2-3.5-2.5 1a7 7 0 0 0-1.7-1L14.9 3h-4l-.4 2.9a7 7 0 0 0-1.7 1l-2.5-1-2 3.5L6.4 11a7.5 7.5 0 0 0 0 2l-2.1 1.6 2 3.5 2.5-1a7 7 0 0 0 1.7 1l.4 2.9h4l.4-2.9a7 7 0 0 0 1.7-1l2.5 1 2-3.5zM12.9 15.5a3.5 3.5 0 1 1 0-7 3.5 3.5 0 0 1 0 7z"/></svg>
    <svg width="20" height="20" viewBox="0 0 24 24" aria-label="Nachrichten"><path fill="var(--cyan)" d="M2 3h20v15H8l-5 4v-4H2z"/><circle cx="8" cy="10.5" r="1.4" fill="#151414"/><circle cx="12" cy="10.5" r="1.4" fill="#151414"/><circle cx="16" cy="10.5" r="1.4" fill="#151414"/></svg>
  </nav>
</section>

<section class="screen screen--cancel">
  <svg class="dial" width="180" height="180" viewBox="0 0 180 180" aria-label="Countdown 4 Sekunden">
    <circle cx="90" cy="90" r="80" fill="none" stroke="var(--ring)" stroke-width="22"/>
    <circle cx="90" cy="90" r="80" fill="none" stroke="var(--alarm)" stroke-width="22" stroke-dasharray="150 353" transform="rotate(-100 90 90)" opacity="0.9"/>
    <circle cx="90" cy="90" r="58" fill="#240304"/>
    <circle cx="90" cy="90" r="42" fill="var(--alarm)"/>
    <text x="90" y="104" text-anchor="middle" font-family="Figtree, sans-serif" font-weight="900" font-size="46" fill="#a80e12">4</text>
    <text x="90" y="122" text-anchor="middle" font-family="Figtree, sans-serif" font-size="10" fill="#a80e12">Sec</text>
  </svg>
  <h2 class="screen-title cancel-title">ALARM<br>ABBRECHEN</h2>
  <nav class="toolbar">
    <svg width="20" height="20" viewBox="0 0 24 24" aria-label="Einstellungen"><path fill="var(--cyan)" d="M19.4 13a7.5 7.5 0 0 0 0-2l2.1-1.6-2-3.5-2.5 1a7 7 0 0 0-1.7-1L14.9 3h-4l-.4 2.9a7 7 0 0 0-1.7 1l-2.5-1-2 3.5L6.4 11a7.5 7.5 0 0 0 0 2l-2.1 1.6 2 3.5 2.5-1a7 7 0 0 0 1.7 1l.4 2.9h4l.4-2.9a7 7 0 0 0 1.7-1l2.5 1 2-3.5zM12.9 15.5a3.5 3.5 0 1 1 0-7 3.5 3.5 0 0 1 0 7z"/></svg>
    <svg width="20" height="20" viewBox="0 0 24 24" aria-label="Nachrichten"><path fill="var(--cyan)" d="M2 3h20v15H8l-5 4v-4H2z"/><circle cx="8" cy="10.5" r="1.4" fill="#151414"/><circle cx="12" cy="10.5" r="1.4" fill="#151414"/><circle cx="16" cy="10.5" r="1.4" fill="#151414"/></svg>
  </nav>
</section>

<section class="screen screen--office">
  <svg class="dial" width="180" height="180" viewBox="0 0 180 180" aria-label="Countdown 4 Sekunden">
    <circle cx="90" cy="90" r="80" fill="none" stroke="var(--ring)" stroke-width="22"/>
    <circle cx="90" cy="90" r="80" fill="none" stroke="var(--alarm)" stroke-width="22" stroke-dasharray="150 353" transform="rotate(-100 90 90)" opacity="0.9"/>
    <circle cx="90" cy="90" r="58" fill="#240304"/>
    <circle cx="90" cy="90" r="42" fill="var(--alarm)"/>
    <text x="90" y="104" text-anchor="middle" font-family="Figtree, sans-serif" font-weight="900" font-size="46" fill="#a80e12">4</text>
    <text x="90" y="122" text-anchor="middle" font-family="Figtree, sans-serif" font-size="10" fill="#a80e12">Sec</text>
  </svg>
  <p class="office-label">Sekretariat:</p>
  <h2 class="screen-title office-title">BITTE BLEIBEN SIE<br>WO SIE SIND</h2>
  <nav class="toolbar">
    <svg width="20" height="20" viewBox="0 0 24 24" aria-label="Einstellungen"><path fill="var(--cyan)" d="M19.4 13a7.5 7.5 0 0 0 0-2l2.1-1.6-2-3.5-2.5 1a7 7 0 0 0-1.7-1L14.9 3h-4l-.4 2.9a7 7 0 0 0-1.7 1l-2.5-1-2 3.5L6.4 11a7.5 7.5 0 0 0 0 2l-2.1 1.6 2 3.5 2.5-1a7 7 0 0 0 1.7 1l.4 2.9h4l.4-2.9a7 7 0 0 0 1.7-1l2.5 1 2-3.5zM12.9 15.5a3.5 3.5 0 1 1 0-7 3.5 3.5 0 0 1 0 7z"/></svg>
    <svg width="20" height="20" viewBox="0 0 24 24" aria-label="Nachrichten"><path fill="var(--cyan)" d="M2 3h20v15H8l-5 4v-4H2z"/><circle cx="8" cy="10.5" r="1.4" fill="#151414"/><circle cx="12" cy="10.5" r="1.4" fill="#151414"/><circle cx="16" cy="10.5" r="1.4" fill="#151414"/></svg>
  </nav>
</section>

</body>
</html>
```